Business Card for Dental Office
Quillbrook Dental
Project: Business Card for Dental Office
Business Card for Dental Office - Health
Creative Brief
Modern
Dr. Walter E Brisk, DDS
Dentist
4175 Delmora Ave, Suite 6C McAllen, TX 78519
quillbrookdental4175@mailvane.test
www.quillbrookdentalclinic.test
This will be printed on a plastic business card. Have not chosen whether it will be transparent, translucent, or black. I am open to suggestions. If a color were to be chosen for the card besides transparent/translucent, the card can be double sided. I am looking for something that impresses patients and potential clients.
MeltavRose MeltavRose
Since the contest is nearing an end, we would like to highlight to strengths of the original designs. #94 is closest to what we're looking for. Adding nice stationary would make it the winner. #120/121, please remove appointment segment on the back since these cards will be made of plastic. If an appointment card were to be made, we would like the same black background (we will use grey shiny pencils to write appointments) #148 stationary is closest to what we're looking for. Looking for modern, simple design on stationary that can be compatible with black & white printing as needed.
We're looking for a predominantly or all-black background design that can make our logo stand out.
Based on what I'm seeing so far, here's some insight on the design: - Logo should stand out - Should be organized - Should stand out (not look like your traditional business card)
The title is incorrect, it is actually business card/stationary for dental office.

```html
<!DOCTYPE html>
<html lang="en">
<head>
<meta charset="utf-8">
<title>Quillbrook Dental Stationery</title>
<link rel="stylesheet" href="https://fonts.googleapis.com/css2?family=Oswald:wght@500&family=Open+Sans:wght@400;600&display=swap">
<style>
:root{
  --stage:#3b3b3d;
  --stage-dark:#242426;
  --ink:#0d0d0d;
  --ink-soft:#1b1b1b;
  --paper:#f4f4f4;
  --accent:#e6451c;
  --muted:#8a8a8a;
  --text-light:#e8e8e8;
}
*{box-sizing:border-box;margin:0;padding:0}
html,body{width:1200px;height:257px;overflow:hidden}
body{
  position:relative;
  background:radial-gradient(ellipse at 50% 40%,var(--stage) 0%,var(--stage-dark) 100%);
  font-family:"Open Sans",sans-serif;
}
.piece{position:absolute;box-shadow:0 3px 8px rgba(0,0,0,.55);overflow:hidden}
.dark{background:linear-gradient(160deg,var(--ink-soft),var(--ink))}
.light{background:var(--paper)}
.brand{display:flex;align-items:center;gap:3px;font-family:"Oswald",sans-serif;font-weight:500;color:var(--accent);white-space:nowrap;line-height:1}
.brand-dot{border-radius:50%;background:var(--accent);flex:none}
.tiny{font-size:3.2px;line-height:1.5;color:var(--muted);white-space:nowrap}
.tiny-light{font-size:3.2px;line-height:1.5;color:var(--text-light);white-space:nowrap}
.band{position:absolute;left:0;right:0;background:var(--accent)}

.card-front{left:24px;top:46px;width:150px;height:86px;display:flex;flex-direction:column;justify-content:center;align-items:center}
.card-front .brand{font-size:15px}
.card-front .brand-dot{width:12px;height:12px}
.card-front .tagline{font-size:4px;color:var(--text-light);margin-top:4px;letter-spacing:.5px}
.card-back{left:24px;top:142px;width:150px;height:86px;padding:10px}
.card-back .name{font-family:"Oswald",sans-serif;font-size:7px;color:var(--text-light)}
.card-back .role{font-size:4.5px;color:var(--accent);margin-bottom:6px}
.card-back .band{bottom:0;height:5px}

.letterhead{left:188px;top:22px;width:95px;height:212px;padding:8px}
.letterhead .brand{font-size:7px}
.letterhead .brand-dot{width:6px;height:6px}
.letterhead .body{margin-top:26px}
.letterhead .body p{margin-bottom:3px}
.letterhead .band{bottom:0;height:6px}
.letterhead .footer{position:absolute;bottom:9px;left:4px;right:4px;text-align:center}

.form-sheet{left:294px;top:22px;width:95px;height:212px;padding:8px}
.form-sheet .brand{font-size:7px}
.form-sheet .brand-dot{width:6px;height:6px}
.form-sheet .title{font-family:"Oswald",sans-serif;font-size:5px;color:var(--ink);margin:14px 0 4px}
.form-row{display:flex;align-items:flex-end;gap:3px;margin-bottom:5px}
.form-row span{font-size:3.2px;color:var(--muted);width:12px}
.form-row i{flex:1;border-bottom:.5px solid #bdbdbd;height:3px}
.form-sheet .band{bottom:0;height:6px}

.mini-card{left:410px;top:34px;width:84px;height:48px;display:flex;align-items:center;justify-content:center}
.mini-card .brand{font-size:8px}
.mini-card .brand-dot{width:6px;height:6px}

.envelope{left:410px;top:94px;width:148px;height:78px}
.envelope .flap{position:absolute;left:0;top:0;width:52px;height:24px;background:var(--accent)}
.envelope .return{position:absolute;left:6px;top:28px}
.envelope .return .brand{font-size:6px}
.envelope .return .brand-dot{width:5px;height:5px}
.envelope-dark{left:410px;top:180px;width:148px;height:54px}
.envelope-dark svg{position:absolute;inset:0}

.folder{left:578px;top:22px;width:96px;height:212px}
.folder-open{left:680px;top:22px;width:96px;height:212px}
.pocket{position:absolute;left:0;right:0;bottom:0;height:70px;background:var(--ink-soft);border-top:1px solid var(--accent)}
.folder-cover{left:788px;top:22px;width:110px;height:212px;display:flex;flex-direction:column;align-items:center;justify-content:center}
.folder-cover .brand{font-size:11px}
.folder-cover .brand-dot{width:9px;height:9px}
.folder-cover .tagline{font-size:4px;color:var(--text-light);margin-top:5px}
.folder-cover .band{bottom:0;height:6px}

.disc{position:absolute;width:88px;height:88px;border-radius:50%;box-shadow:0 3px 8px rgba(0,0,0,.55);display:flex;flex-direction:column;align-items:center;justify-content:center}
.disc::after{content:"";position:absolute;left:36px;top:36px;width:12px;height:12px;border-radius:50%;background:var(--stage-dark)}
.disc .brand{font-size:6px;margin-bottom:26px}
.disc .brand-dot{width:5px;height:5px}
.disc .label{position:absolute;bottom:16px;font-size:3.6px;color:var(--text-light)}
.disc-a{left:960px;top:26px;border:2px solid var(--accent)}
.disc-b{left:1080px;top:26px;border:2px solid var(--ink-soft)}

.appt-card{top:150px;width:100px;height:58px;padding:7px}
.appt-card .brand{font-size:7px}
.appt-card .brand-dot{width:5px;height:5px}
.appt-card .band{bottom:0;height:4px}
.appt-a{left:960px}
.appt-b{left:1076px}
</style>
</head>
<body>

<div class="piece dark card-front">
  <div class="brand"><span class="brand-dot"></span>Quillbrook Dental</div>
  <div class="tagline">Dr. Walter E Brisk, DDS</div>
</div>

<div class="piece dark card-back">
  <div class="name">Dr. Walter E Brisk, DDS</div>
  <div class="role">Dentist</div>
  <div class="tiny-light">4175 Delmora Ave, Suite 6C Brinmoor Falls 40417</div>
  <div class="tiny-light">quillbrookdental4175@mailvane.test</div>
  <div class="tiny-light">www.quillbrookdentalclinic.test</div>
  <div class="band"></div>
</div>

<div class="piece light letterhead">
  <div class="brand"><span class="brand-dot"></span>Quillbrook Dental</div>
  <div class="body tiny">
    <p>Dear Patient,</p>
    <p>Thank you for visiting our clinic today.</p>
    <p>We look forward to your next visit.</p>
    <p>Sincerely,</p>
  </div>
  <div class="footer tiny">4175 Delmora Ave, Suite 6C Brinmoor Falls 40417</div>
  <div class="band"></div>
</div>

<div class="piece light form-sheet">
  <div class="brand"><span class="brand-dot"></span>Quillbrook Dental</div>
  <div class="title">Patient Form</div>
  <div class="form-row"><span>Name</span><i></i></div>
  <div class="form-row"><span>Date</span><i></i></div>
  <div class="form-row"><span>Notes</span><i></i></div>
  <div class="form-row"><span></span><i></i></div>
  <div class="form-row"><span></span><i></i></div>
  <div class="band"></div>
</div>

<div class="piece dark mini-card">
  <div class="brand"><span class="brand-dot"></span>Quillbrook Dental</div>
</div>

<div class="piece light envelope">
  <div class="flap"></div>
  <div class="return">
    <div class="brand"><span class="brand-dot"></span>Quillbrook Dental</div>
    <div class="tiny">4175 Delmora Ave, Suite 6C Brinmoor Falls 40417</div>
  </div>
</div>

<div class="piece dark envelope-dark">
  <svg width="148" height="54" viewBox="0 0 148 54">
    <polyline points="0,0 74,30 148,0" fill="none" stroke="#2c2c2c" stroke-width="1"/>
    <rect x="0" y="50" width="148" height="4" fill="#e6451c"/>
  </svg>
</div>

<div class="piece dark folder"><div class="pocket"></div></div>
<div class="piece dark folder-open"><div class="pocket"></div></div>

<div class="piece dark folder-cover">
  <div class="brand"><span class="brand-dot"></span>Quillbrook Dental</div>
  <div class="tagline">Smile with confidence</div>
  <div class="band"></div>
</div>

<div class="disc dark disc-a">
  <div class="brand"><span class="brand-dot"></span>Quillbrook Dental</div>
  <div class="label">Patient Records</div>
</div>
<div class="disc dark disc-b">
  <div class="brand"><span class="brand-dot"></span>Quillbrook Dental</div>
</div>

<div class="piece dark appt-card appt-a">
  <div class="brand"><span class="brand-dot"></span>Quillbrook Dental</div>
  <div class="band"></div>
</div>
<div class="piece dark appt-card appt-b">
  <div class="tiny-light">Dr. Walter E Brisk, DDS</div>
  <div class="tiny-light">www.quillbrookdentalclinic.test</div>
  <div class="band"></div>
</div>

</body>
</html>
```